Kavoni. Sunless Tanning Mousse Label

I'm looking for a label creation for a new brand of sunless tanning solutions. They are in 6.7oz bottles (template attached).

For the front of the bottle (see template) I would like an abstract multi coloured design taking up just over half the top of the bottle (approx 60%) and going around the design (this is similar to the design inspiration attached). I would this design to use the attached colour palette of pinks. It can be swirls, drips, squares, lines, whatever you think will look good.

The logo will then be over top of that abstract design in the upper 1/3, in the colour #3fe0d0

Under the abstract design the following text:

Wild Plume (Larger text)
Coral Drift (2nd heading)
1 Hour Sunless Mousse (Sub text)
The No Orange Guarantee! (Sub text)
Vegan Formula (sub text)

The sub texts for above can be fun, have coloured background, different fonts, whatever looks good and is sill fun.

Towards the bottom of the front of bottle we require the sizing information:

200ml 6.7 Fl Oz

On the left side of the front (so in the template the middle smaller section) I would like the phrase "You ain't gotta get ready if you stay ready" Could you please make this as a separate little quote, with a fun design to it. It's like a little hidden gem on the side of the bottle.

On the back of the bottle for now can you please start towards the top with:

Wild Plume Mousse (larger)
Coral drift (second heading)
Deep Mediterranean Inspired Tan (second heading)
Easy to Apply & Streak Free
Vegan friendly & 100% natural DHA tan actives

Under this I require approx 1.5" of Lorem Ipsum for now which will take the place of directions for using the product.

Under that in small writing can we include "Warning: This product does not contain a sunscreen and will not protect against sunburn. For external use only. If skin irritation occurs, discontinue use. Carry out a patch test 24 hours prior to full body use. Store below 25(degrees sign)C."

At the bottom is the smallest yet still legible writing, can we include the ingredients that are listed below.

Target Market(s)

Females 24-35 who take care of themselves and always want to look good. It's a youthful fun product.

Requirements
Must have
• Bright colours, and just screams FUN and youthful.

Ingredients must be listed on the back. They dont' need to take up more than an inch in height, less if possible.
*******************************************

INGREDIENTS: Water (Aqua), Propylene Glycol, Dihydroxyacetone, Peg-6 Caprylic/Capric Glycerides, Dihydroxypropyl Peg-5 Linoleammonium Chloride, Peg-7 Glyceryl Cocoate, Caramel,
Phenoxyethanol, Caprylyl Glycol, Potassium Sorbate, Hexylene Glycol, Glycerin, Helianthus Annuus (Sunflower) Seed Oil, Beta Vulgaris (Beet) Root Extract, Panthenol, Solanum Lycopersicum
(Tomato) Fruit Extract, Vaccinium Macrocarpon (Cranberry) Fruit Extract, L-ascorbic Acid (Vitamin C), Tocopheryl Acetate (Vitamin E), Theobroma Cacao (Cocoa) Seed Butter, Rosa Canina (Rose Hip)
Fruit Oil, Glycine Soja (Soybean) Oil, Cucumis Sativus (Cucumber) Fruit Extract, Blue 1 (CI 42090), Red 40 (CI 16035), Yellow 6 (CI 15985), Green 5 (CI 61570), Yellow 5 (CI 19140), Red 33 (CI 17200)

*****************************
Nice to have
• Several options to choose from, some can include a gradient into geometric shapes, rather than solid colour. Experiment
Should not have
• Do not want it to look medical.
Want colours to stay in the same pink family for the abstract design - can use white also.

```html
<!DOCTYPE html>
<html lang="en">
<head>
<meta charset="UTF-8">
<title>Kavoni — Wild Plume Sunless Mousse Label</title>
<link rel="stylesheet" href="https://fonts.googleapis.com/css2?family=Oswald:wght@500;700&family=Great+Vibes&family=Roboto:wght@300;500&display=swap">
<style>
  :root {
    --canvas: #efefef;
    --label: #ffffff;
    --logo-ink: #1d5c5a;
    --teal: #4fbab2;
    --teal-soft: #5cc4bb;
    --plum: #8c2a6e;
    --sub-ink: #4aa9a2;
    --pattern-a: #f7d9d4;
    --pattern-b: #f4ecc8;
    --pattern-c: #d9efe9;
    --pattern-d: #f3cfe0;
  }
  * { margin: 0; padding: 0; box-sizing: border-box; }
  html, body {
    width: 1200px;
    height: 1200px;
    overflow: hidden;
    background: var(--canvas);
  }
  .canvas {
    position: relative;
    width: 1200px;
    height: 1200px;
  }
  .label {
    position: absolute;
    left: 380px;
    top: 50px;
    width: 440px;
    height: 1100px;
    background: var(--label);
    box-shadow: 0 2px 10px rgba(0,0,0,0.06);
    overflow: hidden;
  }
  .label__pattern {
    position: absolute;
    left: 0;
    top: 0;
    width: 440px;
    height: 540px;
  }
  .label__brand {
    position: absolute;
    left: 62px;
    top: 168px;
    font-family: "Oswald", sans-serif;
    font-weight: 700;
    font-size: 96px;
    line-height: 1;
    letter-spacing: 2px;
    color: var(--logo-ink);
  }
  .label__info {
    position: absolute;
    left: 0;
    top: 540px;
    width: 100%;
    display: flex;
    flex-direction: column;
    align-items: center;
    text-align: center;
  }
  .size-pill {
    background: var(--teal-soft);
    color: #ffffff;
    font-family: "Roboto", sans-serif;
    font-weight: 500;
    font-size: 25px;
    padding: 6px 22px;
    border-radius: 24px;
    border: 3px solid #d9f1ee;
  }
  .product-name {
    margin-top: 6px;
    font-family: "Oswald", sans-serif;
    font-weight: 500;
    font-size: 80px;
    line-height: 1.05;
    color: var(--teal);
  }
  .variant-name {
    margin-top: 0;
    font-family: "Great Vibes", cursive;
    font-size: 44px;
    line-height: 1.1;
    color: var(--plum);
  }
  .claims {
    margin-top: 18px;
    list-style: none;
    font-family: "Roboto", sans-serif;
    font-weight: 300;
    font-size: 28px;
    line-height: 48px;
    color: var(--sub-ink);
  }
</style>
</head>
<body>
  <main class="canvas">
    <section class="label">
      <svg class="label__pattern" viewBox="0 0 440 540" role="img" aria-label="Abstract pastel floral pattern panel tapering to a point below the brand name">
        <defs>
          <linearGradient id="patternTone" x1="0" y1="0" x2="1" y2="1">
            <stop offset="0" stop-color="var(--pattern-a)"/>
            <stop offset="0.35" stop-color="var(--pattern-b)"/>
            <stop offset="0.7" stop-color="var(--pattern-c)"/>
            <stop offset="1" stop-color="var(--pattern-d)"/>
          </linearGradient>
        </defs>
        <polygon points="0,0 440,0 440,390 220,540 0,390" fill="url(#patternTone)"/>
      </svg>

      <div class="label__brand">Kavoni.</div>

      <div class="label__info">
        <div class="size-pill">200ml 6.7 Fl Oz</div>
        <h1 class="product-name">Wild Plume</h1>
        <h2 class="variant-name">Coral Drift</h2>
        <ul class="claims">
          <li>Hour Sunless Mousse</li>
          <li>The No Orange Guarantee!</li>
          <li>Vegan Formula</li>
        </ul>
      </div>
    </section>
  </main>
</body>
</html>
```